We need your help in designing the graphical look of the home page of our web site: Quellnest.com.

Quellnest is an FREE online service that brings consumers and service providers together through online reservations.

Our service is in fact a web application (similar to brindlo calendar), so we will be using forms, widgets, menus and standard web controls (buttons, fields, links, etc). We need a design that will be easy to integrate with our programming.

This design project is for the HOME page, but we will choose the designer that will design the web page in photoshop in layers, so we can easily derive our other secondary pages ourselves.

If you have any questions please send us a message and we will gladly update the brief with a response.

Happy Designing!
Updates

Hi all, the menu on the home page should be something standard, like: Pricing, features, how it works.

once a user is logged in, they will see their toolbox at all times:
- My Nest (links to their main page of bookings)
- My Faborites (view favorite businesses and book quickly with them)
- Settings (set parameters of their account)

There should be a My Profile page as well. 

Thanks!

Reason: I have extended the deadline to receive more designs.

Hi All,

UPDATE: we changed our vision of the home page to have a much simpler design.  something along the lines of tumbrella vexnor and mor tan.

HOME PAGE:
light colors with white background.  simple, simple, simple!

header should not be big, logo, change language link. try with search bar (what and where).

body should be simple, with an image + register form only.

footer with links to pages for more info:
- Privacy,
- Getting started
- How it works
- Contact us
- FAQ
- Pricing

LOGGED IN PAGE:
when logged in, the header can be the same or reduced to maximize the "working area" (body).
body can be a 2 or 3 column design, as we have a main working area.  in your design, show a calendar.  we need a toolbar (side or top) that will have these buttons, links: MyNest, My Favorites, Settings, My Profile.
We need a section that will display latest messages or notifications.
keep the footer with the links.

Thank you all.

Reason: Holidays

Reason: holidays... lets spend time with our families!

Target Market(s)

Young and mobile consumers + professionals, businesses, restaurants and commerces wishing to offer online reservations (appointments and reservations)

Industry/Entity Type

Brindlo

Requirements
Must have
• - Easy to integrate with web programming
- light weight visual design. We want something with light tone colors as background
- home page will have a content slider that will show some catch phrases.
- Overall design should be more on the "cartoony" side. Should give a casual, humour and friendly ambiance.

The home page should have these sections:
- a search section for consumers to find local businesses. They will search by specifying "What?" & "Where?"
- a content slider that will cycle through catch phrases and features. Each pane should have an image representative of the text.
- have 4 highlighted sections
- QuellNest is great for (list of different businesses types that use quelnest)
- QuellNest is available for FREE to everyone
- Main features list (accept 24/7 reservations, never reveal your schedule, automatic reminders, marketing campaigns)
- The more you quell, the more you save! (info on our loyalty program that entitles consumers to greater savings and benefits).

One a user logs in, all the certer page info will be replaced by a content div that will allow content to display based on selected menu item
- My Nest (opens the main section where all happens. This section should have a design that gives the impression that we're looking in a box)
- My Profile
- My Favorites
Should not have
• - Don't use actual photos of real people, rather opt for sketches and cartoony characters.

```html
<!DOCTYPE html>
<html lang="en">
<head>
<meta charset="utf-8">
<title>QuellNest – Calendar</title>
<link rel="stylesheet" href="https://fonts.googleapis.com/css2?family=Arimo:wght@400;700&display=swap">
<style>
:root{
  --header-bg:#222427;
  --header-line:#8a8c8e;
  --brand:#3aa5c2;
  --field-bg:#f1f1f1;
  --field-text:#777;
  --button-gold:#d9cf94;
  --button-gold-dark:#b9ab62;
  --welcome:#45708f;
  --text:#222;
  --muted:#555;
  --grid-line:#c6c6c6;
  --day-head-line:#bcbcbc;
  --other-month:#aeb4b8;
  --blue:#29b2e2;
  --blue-pale:#d6ecf6;
  --green:#a6e05e;
  --box-tint:#dcecee;
  --footer-band:#c8dfe0;
  --footer-link:#4f7890;
  --social:#253a52;
  --badge-grey:#e4e4e4;
}
*{box-sizing:border-box;margin:0;padding:0}
html,body{width:1200px;height:815px;overflow:hidden;background:#fff}
body{position:relative;font-family:"Arimo",Arial,sans-serif;color:var(--text)}
.box-depth{position:absolute;left:0;top:0;width:1200px;height:815px;z-index:0}
.site-header{position:absolute;left:0;top:0;width:1200px;height:56px;background:var(--header-bg);border-bottom:3px solid var(--header-line);z-index:2}
.brand{position:absolute;left:60px;top:12px;display:flex;align-items:center;gap:8px;color:var(--brand);font-size:21px;font-weight:700;letter-spacing:1px}
.brand-square{width:30px;height:30px;background:var(--brand);border-radius:3px}
.search-label{position:absolute;top:6px;color:#ddd;font-size:12px;font-weight:700}
.search-field{position:absolute;top:25px;height:22px;width:229px;background:var(--field-bg);border:1px solid #999;font-size:12px;color:var(--field-text);padding:3px 7px}
.search-button{position:absolute;left:1052px;top:22px;width:92px;height:26px;border-radius:4px;background:linear-gradient(#ebe3ae,var(--button-gold));border:1px solid var(--button-gold-dark);font-size:15px;text-align:center;line-height:24px;color:#222}
.sidebar{position:absolute;left:58px;top:92px;width:210px;z-index:2}
.welcome{font-size:17px;font-weight:700;color:var(--welcome);height:40px;border-bottom:1px solid #ddd}
.mini-cal{margin-top:8px;border-bottom:1px solid #ddd;padding-bottom:4px}
.mini-head{display:flex;justify-content:space-between;align-items:center;font-size:12px;font-weight:700;height:22px;padding-left:3px}
.mini-arrows{display:flex;gap:3px}
.mini-arrows span{width:15px;height:15px;background:var(--blue-pale);color:#3a8fc0;font-size:12px;line-height:15px;text-align:center;font-weight:700}
.mini-grid{display:grid;grid-template-columns:repeat(7,1fr);font-size:12px;text-align:center;margin-top:2px}
.mini-grid span{height:19px;line-height:19px}
.mini-grid .dow{background:#e6e6e6;font-weight:700;height:21px;line-height:21px}
.mini-grid .other{color:var(--other-month)}
.mini-grid .sel{background:var(--blue-pale);color:#1f7fae;font-weight:700}
.mini-toggle{text-align:center;font-size:12px;color:var(--footer-link);padding-top:4px}
.toolbox{list-style:none;margin-top:6px}
.toolbox li{display:flex;align-items:center;height:34px;border-bottom:1px dotted #bbb;font-size:13px;gap:8px}
.toolbox li svg{width:20px;height:18px;flex:none}
.toolbox .label{flex:1}
.toolbox .note{color:var(--welcome);font-weight:700}
.count{min-width:20px;height:20px;line-height:20px;text-align:center;font-size:11px;font-weight:700;background:var(--badge-grey);color:#8b98a6;border-radius:2px}
.count.hot{background:var(--blue);color:#fff}
.pager{position:absolute;left:288px;top:89px;display:flex;border:1px solid #aaa;border-radius:3px;z-index:2}
.pager span{padding:0 10px;height:26px;line-height:26px;font-size:13px;color:#444}
.pager span+span{border-left:1px solid #aaa}
.month-title{position:absolute;left:439px;top:90px;font-size:23px;font-weight:700;z-index:2}
.views{position:absolute;left:877px;top:89px;display:flex;border:1px solid #aaa;border-radius:3px;overflow:hidden;z-index:2}
.views span{width:66px;height:26px;line-height:26px;text-align:center;font-size:14px;color:#555;background:#fff}
.views span+span{border-left:1px solid #ccc}
.views .on{background:linear-gradient(#5ccbef,var(--blue));color:#fff;font-weight:700}
.calendar{position:absolute;left:288px;top:133px;width:853px;z-index:1}
.cal-days{display:grid;grid-template-columns:repeat(7,1fr);height:27px;border-top:1px solid var(--day-head-line);border-bottom:1px solid var(--day-head-line);font-size:12px;font-weight:700}
.cal-days span{padding:6px 0 0 7px}
.cal-grid{display:grid;grid-template-columns:repeat(7,1fr);grid-auto-rows:101px;border-left:1px solid var(--grid-line);background:rgba(255,255,255,.55)}
.cal-grid .day{border-right:1px solid var(--grid-line);border-bottom:1px solid var(--grid-line);font-size:12px;font-weight:700;padding:4px 0 0 6px;position:relative}
.cal-grid .other{color:var(--other-month);font-weight:400}
.event{position:absolute;left:1px;right:1px;top:23px;height:21px;font-size:12px;font-weight:400;line-height:21px;padding-left:5px;white-space:nowrap;overflow:hidden}
.event time{font-size:10px;margin-right:6px}
.event.blue{background:var(--blue);color:#fff}
.event.green{background:var(--green);color:#222}
.event-popup{position:absolute;left:662px;top:243px;width:225px;height:106px;background:#fff;border:1px solid #bbb;box-shadow:0 1px 4px rgba(0,0,0,.25);padding:8px 12px;z-index:3}
.event-popup h3{font-size:15px;font-weight:400}
.event-popup .when{font-size:12px;margin-top:4px}
.event-popup p{font-size:10px;color:#666;line-height:1.35;margin-top:8px}
.event-popup .edit{position:absolute;right:12px;bottom:8px;font-size:11px;color:#2b6d99;text-decoration:underline}
.event-popup::before{content:"";position:absolute;left:-7px;top:47px;width:12px;height:12px;background:#fff;border-left:1px solid #bbb;border-bottom:1px solid #bbb;transform:rotate(45deg)}
.site-footer{position:absolute;left:34px;top:730px;width:1132px;height:85px;z-index:2}
.language{position:absolute;left:12px;top:13px;width:88px;height:24px;border:1px solid #999;border-radius:3px;background:linear-gradient(#fff,#e8e8e8);font-size:13px;line-height:22px;padding-left:12px}
.language::after{content:"";position:absolute;right:8px;top:9px;border:5px solid transparent;border-top-color:#555}
.footer-links{position:absolute;left:122px;top:17px;display:flex;font-size:13px;color:var(--footer-link)}
.footer-links span{padding:0 9px;border-left:1px solid #aab}
.footer-links span:first-child{border-left:0}
.follow{position:absolute;left:907px;top:14px;display:flex;align-items:center;gap:6px;font-size:16px;font-weight:700;color:#3a5a74}
.social{display:flex;align-items:center;gap:3px;font-size:10px;font-weight:700;color:var(--social)}
.social i{width:12px;height:12px;background:var(--social);border-radius:2px;display:block}
</style>
</head>
<body>
<svg class="box-depth" viewBox="0 0 1200 815" aria-hidden="true">
  <defs>
    <linearGradient id="tint" x1="0" y1="0" x2="0" y2="1">
      <stop offset="0" stop-color="#eef6f7"/>
      <stop offset="1" stop-color="#d9ebec"/>
    </linearGradient>
  </defs>
  <polygon points="289,292 996,292 1166,730 34,730" fill="url(#tint)"/>
  <rect x="34" y="730" width="1132" height="85" fill="#c6dedf"/>
</svg>

<header class="site-header">
  <div class="brand"><span class="brand-square"></span>QuellNest</div>
  <span class="search-label" style="left:573px">What</span>
  <div class="search-field" style="left:570px">e.g. Italian food, XXXX film</div>
  <span class="search-label" style="left:814px">Where</span>
  <div class="search-field" style="left:812px">e.g. Some Neighborhood</div>
  <div class="search-button">Search</div>
</header>

<aside class="sidebar">
  <div class="welcome">Welcome back, John</div>
  <div class="mini-cal">
    <div class="mini-head">January, 2012<div class="mini-arrows"><span>‹</span><span>›</span></div></div>
    <div class="mini-grid">
      <span class="dow">S</span><span class="dow">M</span><span class="dow">T</span><span class="dow">W</span><span class="dow">T</span><span class="dow">F</span><span class="dow">S</span>
      <span>1</span><span>2</span><span>3</span><span>4</span><span>5</span><span>6</span><span>7</span>
      <span>8</span><span>9</span><span class="sel">10</span><span>11</span><span>12</span><span>13</span><span>14</span>
      <span>15</span><span>16</span><span>17</span><span>18</span><span>19</span><span>20</span><span class="sel">21</span>
      <span>22</span><span>23</span><span>24</span><span>25</span><span>26</span><span>27</span><span>28</span>
      <span>29</span><span>30</span><span>31</span><span class="other">1</span><span class="other">2</span><span class="other">3</span><span class="other">4</span>
    </div>
    <div class="mini-toggle">hide mini calendar</div>
  </div>
  <ul class="toolbox">
    <li><svg viewBox="0 0 20 18"><path d="M4 2v15" stroke="#999" stroke-width="2"/><path d="M5 2h11l-3 4 3 4H5z" fill="#aaa"/></svg><span class="label note">Notification</span><span class="count hot">2</span></li>
    <li><svg viewBox="0 0 20 18"><path d="M2 8l3-6h10l3 6v8H2z" fill="#aaa"/><rect x="6" y="9" width="8" height="3" fill="#eee"/></svg><span class="label">My Nest</span><span class="count">2</span></li>
    <li><svg viewBox="0 0 20 18"><path d="M10 16L2 8a4 4 0 0 1 8-4 4 4 0 0 1 8 4z" fill="#aaa"/></svg><span class="label">My Favorites</span><span class="count">35</span></li>
    <li><svg viewBox="0 0 20 18"><rect x="1" y="4" width="18" height="11" fill="#aaa"/><rect x="3" y="6" width="5" height="6" fill="#eee"/><rect x="10" y="7" width="7" height="2" fill="#eee"/></svg><span class="label">My Profile</span></li>
    <li><svg viewBox="0 0 20 18"><circle cx="10" cy="9" r="6" fill="none" stroke="#aaa" stroke-width="4" stroke-dasharray="3 2"/><circle cx="10" cy="9" r="4" fill="none" stroke="#aaa" stroke-width="2"/></svg><span class="label">Settings</span></li>
  </ul>
</aside>

<div class="pager"><span>&lt; Prev</span><span>Next &gt;</span></div>
<h1 class="month-title">January, 2012</h1>
<div class="views"><span>Day</span><span>Week</span><span class="on">Month</span><span>List</span></div>

<section class="calendar">
  <div class="cal-days"><span>SUN</span><span>MON</span><span>TUE</span><span>WED</span><span>THUR</span><span>FRI</span><span>SAT</span></div>
  <div class="cal-grid">
    <div class="day">1</div><div class="day">2</div><div class="day">3</div><div class="day">4</div><div class="day">5</div><div class="day">6</div><div class="day">7</div>
    <div class="day">8</div><div class="day">9</div><div class="day">10<div class="event blue"><time>20:00</time>Lectus natoqu</div></div><div class="day">11</div><div class="day">12</div><div class="day">13</div><div class="day">14</div>
    <div class="day">15</div><div class="day">16</div><div class="day">17</div><div class="day">18</div><div class="day">19</div><div class="day">20</div><div class="day">21<div class="event green"><time>18:00</time>Dignissim a nu</div></div>
    <div class="day">22</div><div class="day">23</div><div class="day">24</div><div class="day">25</div><div class="day">26</div><div class="day">27</div><div class="day">28</div>
    <div class="day">29</div><div class="day">30</div><div class="day">31</div><div class="day other">1</div><div class="day other">2</div><div class="day other">3</div><div class="day other">4</div>
  </div>
</section>

<div class="event-popup">
  <h3>Lectus natoque blak</h3>
  <div class="when">Tuesday | Jan 10th, 2012 | 20:00</div>
  <p>Quis arcu adipiscing nec pid? Elit duis sed. Vel magnis pid et!</p>
  <span class="edit">Edit »</span>
</div>

<footer class="site-footer">
  <div class="language">English</div>
  <nav class="footer-links"><span>Privacy</span><span>Getting Started</span><span>How It Works</span><span>Contact Us</span><span>FAQ</span><span>Pricing</span></nav>
  <div class="follow">Follow Us:
    <span class="social"><i></i>Tumbrella</span>
    <span class="social"><i></i>Vexnor</span>
    <span class="social"><i></i>Brindlo</span>
  </div>
</footer>
</body>
</html>
```